Law Firm Letterhead

We are looking for a letterhead for our military/veterans law firm. We like simplicity and clean, modern, flat, uncluttered designs. Our logo font is DIN 1451, and our website/business card info font is Helvetica Neue.

Required Information:

- Logo/Graphic: Please see attached logo / business card for ideas. Please also review firm website.

- Motto: A law firm for service members and veterans

- Web Address: www.harborlinecounsel.com

- Email: info@harborlinecounsel.com

- Phone: 866-402-1953

Colors: We prefer either a blue/grey or an all-blue color scheme. The blue in our logo is #336699.

Please DO NOT submit more than 3 designs. Spamming designs with only minor changes between the designs is not appreciated. We can evaluate your quality and direction by your best 1 or 2 designs.

Thank you!

```html
<!DOCTYPE html>
<html lang="en">
<head>
<meta charset="utf-8">
<title>Harborline Counsel Letterhead</title>
<link rel="stylesheet" href="https://fonts.googleapis.com/css2?family=Roboto:wght@400&family=Roboto+Condensed:wght@700&family=Tinos:ital,wght@0,400;0,700;1,400&display=swap">
<style>
  :root {
    --brand-blue: #2d5f95;
    --paper: #f1f2f4;
    --backdrop: #ddd6cf;
    --ink: #3a3a3a;
  }
  html, body {
    margin: 0;
    width: 1200px;
    height: 975px;
    overflow: hidden;
    background: var(--backdrop);
  }
  .letterhead {
    position: absolute;
    left: 282px;
    top: 37px;
    width: 636px;
    height: 900px;
    background: var(--paper);
    box-shadow: 0 4px 18px rgba(0,0,0,0.12);
    overflow: hidden;
  }
  .corner-accent {
    position: absolute;
    top: 0;
    right: 0;
  }
  .firm-name {
    position: absolute;
    top: 120px;
    left: 190px;
    display: flex;
    align-items: center;
    gap: 10px;
    font-family: "Roboto Condensed", sans-serif;
    font-weight: 700;
    font-size: 28px;
    line-height: 1;
    letter-spacing: 1px;
    text-transform: uppercase;
    color: var(--brand-blue);
    white-space: nowrap;
  }
  .firm-name .mark {
    width: 20px;
    height: 20px;
    background: var(--brand-blue);
  }
  .letter-body {
    position: absolute;
    top: 215px;
    left: 240px;
    width: 320px;
    font-family: "Tinos", serif;
    font-size: 10.5px;
    line-height: 1.45;
    color: var(--ink);
    text-align: justify;
  }
  .letter-body h2 {
    margin: 0 0 8px;
    font-family: "Tinos", serif;
    font-size: 11px;
    letter-spacing: 0.5px;
    font-weight: 400;
    color: var(--brand-blue);
  }
  .letter-body p { margin: 0 0 9px; }
  .letter-body .lead { font-weight: 700; }
  .letter-body .closing { font-style: italic; font-size: 9.5px; }
  .footer-band {
    position: absolute;
    left: 0;
    bottom: 0;
    width: 100%;
    height: 118px;
    background: var(--brand-blue);
    color: #ffffff;
    font-family: "Roboto", sans-serif;
  }
  .contact-row {
    position: absolute;
    top: -22px;
    left: 36px;
    right: 36px;
    display: flex;
    justify-content: space-between;
    font-size: 11px;
    color: var(--brand-blue);
  }
  .motto {
    position: absolute;
    top: 50px;
    width: 100%;
    text-align: center;
    font-size: 20px;
    letter-spacing: 0.3px;
  }
</style>
</head>
<body>
  <main class="letterhead">
    <svg class="corner-accent" width="190" height="300" viewBox="0 0 190 300" aria-hidden="true">
      <polygon points="0,0 190,0 190,300" fill="var(--brand-blue)"/>
    </svg>

    <div class="firm-name"><span class="mark"></span>Harborline Counsel</div>

    <article class="letter-body">
      <h2>HARBORLINE</h2>
      <p><span class="lead">Dear client, thank you for trusting our team with your case.</span> We review every file with care and respond within two business days. Our attorneys focus on benefits, discharge upgrades and military justice matters for members of every branch.</p>
      <p>Please keep this letter with your records. If any detail changes, contact our office so we can update your file and keep your claim moving forward without delay.</p>
      <p class="closing">We look forward to working with you.</p>
    </article>

    <footer class="footer-band">
      <div class="contact-row">
        <span>info@harborlinecounsel.com</span>
        <span>www.harborlinecounsel.com</span>
        <span>866-402-1953</span>
      </div>
      <div class="motto">a law firm for service members and veterans</div>
    </footer>
  </main>
</body>
</html>
```